A ebook cover to reinvent the imagery of vegetable companion gardening

We needs a ebook design with illustrates minimal as well as clear and concise relevance to vegetable companion gardening . we will add a mock up design and other existing designs to help you gauge and create the sort of illustration fit for our aims.
Book Title: Harvest Patch Basics – Vegetable Partner Sowing
Subtitle: Partner Handbook For Raising Crops Through Simple, Natural & Lasting Plot Methods
(Perfect For Beginners)
Author: Tall Meadow
Size: 5.5 x 8.5

```html
<!DOCTYPE html>
<html lang="en">
<head>
<meta charset="utf-8">
<title>Harvest Patch Basics – Vegetable Partner Sowing</title>
<link rel="stylesheet" href="https://fonts.googleapis.com/css2?family=Poppins:wght@400;500;700&display=swap">
<style>
  :root {
    --page-bg: #f0f0f0;
    --cover-top: #03060d;
    --cover-mid: #1d2630;
    --cover-bottom: #02040a;
    --accent-orange: #f26a21;
    --accent-green: #6db544;
    --text-light: #ffffff;
    --art-warm: #a0522d;
    --art-deep: #5c3a1e;
  }
  * { margin: 0; padding: 0; box-sizing: border-box; }
  html, body {
    width: 686px;
    height: 1200px;
    overflow: hidden;
    background: var(--page-bg);
    font-family: "Poppins", sans-serif;
  }
  .cover {
    position: absolute;
    left: 23px;
    top: 105px;
    width: 640px;
    height: 989px;
    background: linear-gradient(180deg, var(--cover-top) 0%, var(--cover-top) 24%, var(--cover-mid) 50%, var(--cover-mid) 68%, var(--cover-bottom) 86%);
    box-shadow: 0 2px 8px rgba(0,0,0,0.18);
    color: var(--text-light);
    text-align: center;
  }
  .cover__title {
    position: absolute;
    top: 40px;
    left: 0;
    width: 100%;
    font-weight: 400;
    font-size: 78px;
    line-height: 1;
  }
  .cover__title-line { display: block; }
  .cover__title-line--second { font-weight: 500; }
  .word--orange { color: var(--accent-orange); }
  .word--green { color: var(--accent-green); }
  .cover__series {
    position: absolute;
    top: 228px;
    left: 0;
    width: 100%;
    font-size: 26px;
    font-weight: 700;
    line-height: 1.2;
  }
  .cover__art {
    position: absolute;
    left: 60px;
    top: 320px;
    width: 520px;
    height: 430px;
    border-radius: 28px;
    background: linear-gradient(180deg, var(--art-warm) 0%, var(--art-deep) 100%);
  }
  .cover__tagline {
    position: absolute;
    top: 802px;
    left: 80px;
    width: 480px;
    font-size: 19px;
    font-weight: 700;
    line-height: 23.5px;
  }
  .cover__author {
    position: absolute;
    top: 890px;
    left: 0;
    width: 100%;
    font-size: 38px;
    font-weight: 400;
    line-height: 1.2;
    letter-spacing: 3px;
    color: var(--accent-green);
  }
</style>
</head>
<body>
  <main class="cover">
    <h1 class="cover__title">
      <span class="cover__title-line"><span class="word--orange">Harvest</span> Patch</span>
      <span class="cover__title-line cover__title-line--second"><span class="word--green">Basics</span></span>
    </h1>
    <p class="cover__series">VEGETABLE PARTNER SOWING</p>
    <div class="cover__art" role="img" aria-label="Woven wicker basket filled with peppers, squash, tomatoes, grapes, oranges and leafy greens"></div>
    <p class="cover__tagline">Partner Handbook For Raising Crops Through Simple, Natural &amp; Lasting Plot Methods</p>
    <p class="cover__author">TALL MEADOW</p>
  </main>
</body>
</html>
```